Healthcare Technology Presentation Folder + Proposal Front Page + Letter Head

We require someone to come up with stationery design theme the following

- Presentation Folders - Template supplied
- Proposal Front Page - A4
- Letter Head - A4

I've provided our company logo, and also the presentation folder template to use.
The Letter head template and Proposal front page design is to be provided in Microsoft Word. Presentation Folder to be provided on the template we have supplied or so long as the dimensions match.

We are looking for a new fresh look, professional design with our target audience being healthcare professionals. Prefer the colour scheme of our logo and traditional black

The presentation folder is to look professional, have our website address tralvenhub.com.au and no other information. Some nice accompanying graphics.

The Letter Head / Proposal Front page must have the following information
- Our logo
- Suite 31, 218 Wexcombe Street
Port Melbourne, Victoria, 3184
- Phone: 03 9472 6358
- Fax: 03 8215 4937
- Web: tralvenhub.com.au

The winning design must contain all three designs with a consistent look and feel

Target Market(s)

Healthcare Professional

Font styles to use
Sans Serif

Requirements
Must have
• Our company colours
Should not have
• Healthcare Symbols

```html
<!DOCTYPE html>
<html lang="en">
<head>
<meta charset="utf-8">
<title>Tralvenhub Letterhead</title>
<link rel="stylesheet" href="https://fonts.googleapis.com/css2?family=Didact+Gothic&display=swap">
<style>
  :root {
    --brand-orange: #e8943e;
    --brand-blue: #3b7aa3;
    --ink: #1f1f1f;
    --paper: #ffffff;
    --edge: #8a8a8a;
  }
  * { margin: 0; padding: 0; box-sizing: border-box; }
  html, body {
    width: 849px;
    height: 1200px;
    overflow: hidden;
    background: var(--paper);
  }
  .letterhead {
    position: relative;
    width: 849px;
    height: 1200px;
    background: var(--paper);
    border: 1px solid var(--edge);
    font-family: "Didact Gothic", "Century Gothic", sans-serif;
    color: var(--ink);
  }
  .brand {
    position: absolute;
    left: 54px;
    top: 72px;
    display: flex;
    align-items: center;
    gap: 14px;
  }
  .brand-mark {
    width: 34px;
    height: 34px;
    background: var(--brand-orange);
  }
  .brand-name {
    font-size: 46px;
    line-height: 1;
    color: var(--brand-blue);
    letter-spacing: -0.5px;
  }
  .contact {
    position: absolute;
    left: 577px;
    top: 52px;
    font-size: 15px;
    line-height: 17.5px;
    list-style: none;
  }
  .contact li {
    display: flex;
    align-items: center;
    gap: 6px;
    white-space: nowrap;
  }
  .contact .icon {
    width: 15px;
    height: 15px;
    flex: none;
    fill: none;
    stroke: var(--brand-orange);
  }
  .contact .icon .solid { fill: var(--brand-orange); stroke: none; }
</style>
</head>
<body>
  <main class="letterhead">
    <header>
      <div class="brand">
        <span class="brand-mark" aria-hidden="true"></span>
        <span class="brand-name">Tralvenhub</span>
      </div>

      <ul class="contact">
        <li>Suite 31, 218 Wexcombe Street</li>
        <li>Port Melbourne, Victoria, 3184</li>
        <li>
          <svg class="icon" viewBox="0 0 16 16" aria-label="Phone">
            <path class="solid" d="M1 6 C1 3 15 3 15 6 L15 7 L11 7 L11 5.5 L5 5.5 L5 7 L1 7 Z"/>
            <path class="solid" d="M4 8 L12 8 L14 13 L2 13 Z"/>
            <circle cx="8" cy="10.5" r="1.4" fill="#fff"/>
          </svg>
          <span>03 9472 6358</span>
        </li>
        <li>
          <svg class="icon" viewBox="0 0 16 16" aria-label="Fax">
            <rect x="4" y="1.5" width="8" height="13" rx="1.5" stroke-width="1.6"/>
            <line x1="7" y1="12" x2="9" y2="12" stroke-width="1.4"/>
          </svg>
          <span>03 8215 4937</span>
        </li>
        <li>
          <svg class="icon" viewBox="0 0 16 16" aria-label="Website">
            <circle class="solid" cx="8" cy="8" r="7"/>
            <g stroke="#fff" stroke-width="0.9" fill="none">
              <ellipse cx="8" cy="8" rx="3" ry="7"/>
              <line x1="1" y1="8" x2="15" y2="8"/>
              <line x1="2" y1="4.5" x2="14" y2="4.5"/>
              <line x1="2" y1="11.5" x2="14" y2="11.5"/>
            </g>
          </svg>
          <span>tralvenhub.com.au</span>
        </li>
      </ul>
    </header>
  </main>
</body>
</html>
```